Lanterne architecture business cards

We are a new company based in New Zealand. We Specialize in High end Luxury Residential Architecture.

Every home is bespoke and is designed to each clients individual requirements and needs.

I like to design buildings that inspire people through light and form while offering a high level of comfort and usability.

Lines of sight, proportion and balance are fundamental to the spaces I create.
Updates

August 5th is current deadline - Today's date is the 13th of August.

Target Market(s)

New Zealanders who want a custom individual home design, typically 30-65 year old males and females

Industry/Entity Type

Architecture

Contact Information for Business Card

Director - Derek Tolson
Contact Number - 0279164073
Email - info@lanternearchitecture-example.co.nz
Webstie - www.lanternearchitecture-example.co.nz
Social Media - @lanternearchitecture

Font styles to use
Sans Serif

Requirements
Must have
• Logo (Both Sides)
Website
Email
Contact Number
Social Media

Nice to have
• Texture
Should not have
• More than 3 colours - typically I would've thought 2 would be good to match the logo.

```html
<!DOCTYPE html>
<html lang="en">
<head>
<meta charset="utf-8">
<title>Lanterne architecture business cards</title>
<link rel="stylesheet" href="https://fonts.googleapis.com/css2?family=Roboto:wght@300;400;500;700&display=swap">
<style>
:root{
  --ink:#111214;
  --card:#ededee;
  --card-edge:#e2e3e4;
  --backdrop:#1f2226;
  --backdrop-alt:#24272c;
  --pattern-a:#e6e7e8;
  --pattern-b:#d9dadc;
}
*{box-sizing:border-box;margin:0;padding:0}
html,body{width:1200px;height:750px;overflow:hidden}
body{background:var(--backdrop);font-family:"Roboto",sans-serif;color:var(--ink)}
.sheet{display:grid;grid-template-columns:repeat(3,400px);grid-template-rows:repeat(2,375px);width:1200px;height:750px}
.cell{display:flex;align-items:center;justify-content:center}
.cell:nth-child(even){background:var(--backdrop-alt)}
.card{position:relative;width:340px;height:196px;background:var(--card);border-radius:12px;overflow:hidden;box-shadow:0 10px 24px rgba(0,0,0,.45)}
.wordmark{font-weight:300;text-transform:uppercase;letter-spacing:.32em;font-size:13px;line-height:1.25;color:var(--ink);white-space:nowrap}
.wordmark small{display:block;font-size:5px;letter-spacing:.55em}
.mark-dot{display:block;width:18px;height:18px;border:2px solid var(--ink);border-radius:50%}
.pattern{position:absolute;inset:0;background:linear-gradient(135deg,var(--pattern-a),var(--pattern-b))}
.back-centre{position:absolute;inset:0;display:flex;flex-direction:column;align-items:center;justify-content:center;gap:8px}
.back-left{position:absolute;left:40px;top:50%;transform:translateY(-50%);display:flex;align-items:center;gap:10px}
.person{position:absolute;text-align:right}
.person .name{font-weight:700;font-size:14px}
.person .role{font-weight:400;font-size:10px}
.contacts{position:absolute;list-style:none;font-size:7px;font-weight:400;line-height:1}
.contacts li{display:flex;align-items:center;gap:6px;height:13px;white-space:nowrap}
.contacts svg{width:9px;height:9px;flex:none}
.rule{position:absolute;left:0;top:0;width:100%;height:100%}
</style>
</head>
<body>
<main class="sheet">

  <section class="cell">
    <div class="card card-back-pattern">
      <div class="pattern" role="img" aria-label="Repeating light grey monogram pattern across the card back"></div>
      <div class="back-centre">
        <span class="mark-dot"></span>
        <span class="wordmark">Lanterne</span>
      </div>
    </div>
  </section>

  <section class="cell">
    <div class="card card-back-plain">
      <div class="back-left">
        <span class="mark-dot"></span>
        <span class="wordmark">Lanterne</span>
      </div>
    </div>
  </section>

  <section class="cell">
    <div class="card card-back-wordmark">
      <div class="back-centre">
        <span class="mark-dot"></span>
        <span class="wordmark">Lanterne<small>Architecture</small></span>
      </div>
    </div>
  </section>

  <section class="cell">
    <div class="card card-front-vertical">
      <svg class="rule" viewBox="0 0 340 196" aria-hidden="true">
        <line x1="160" y1="0" x2="160" y2="88" stroke="#111214" stroke-width="2"/>
        <circle cx="150" cy="100" r="12" fill="none" stroke="#111214" stroke-width="2"/>
        <line x1="160" y1="112" x2="160" y2="196" stroke="#111214" stroke-width="2"/>
      </svg>
      <div style="position:absolute;left:22px;top:48px;display:flex;flex-direction:column;gap:8px;align-items:flex-start">
        <span class="mark-dot"></span>
        <span class="wordmark" style="font-size:12px">Lanterne<small>Architecture</small></span>
      </div>
      <div class="person" style="right:18px;top:62px">
        <div class="name">Derek Tolson</div>
        <div class="role">Director</div>
      </div>
      <ul class="contacts" style="left:170px;top:124px">
        <li><svg viewBox="0 0 10 10"><circle cx="5" cy="5" r="4.4" fill="none" stroke="#111214" stroke-width=".8"/><path d="M3.4 3h1l.4 1-.6.5a3 3 0 0 0 1.3 1.3l.5-.6 1 .4v1a.6.6 0 0 1-.6.6A3.6 3.6 0 0 1 2.8 3.6.6.6 0 0 1 3.4 3z" fill="#111214"/></svg>0279164073</li>
        <li><svg viewBox="0 0 10 10"><circle cx="5" cy="3.2" r="1.8" fill="none" stroke="#111214" stroke-width=".9"/><path d="M1.5 9a3.5 3 0 0 1 7 0" fill="none" stroke="#111214" stroke-width=".9"/></svg>@lanternearchitecture</li>
        <li><svg viewBox="0 0 10 10"><circle cx="5" cy="5" r="4.2" fill="none" stroke="#111214" stroke-width=".9"/><path d="M1 5h8M5 .8c-2 2.4-2 6 0 8.4M5 .8c2 2.4 2 6 0 8.4" fill="none" stroke="#111214" stroke-width=".7"/></svg>www.lanternearchitecture-example.co.nz</li>
        <li><svg viewBox="0 0 10 10"><circle cx="5" cy="5" r="4.2" fill="none" stroke="#111214" stroke-width=".9"/><circle cx="5" cy="5" r="2" fill="none" stroke="#111214" stroke-width=".9"/></svg>info@lanternearchitecture-example.co.nz</li>
      </ul>
    </div>
  </section>

  <section class="cell">
    <div class="card card-front-horizontal">
      <svg class="rule" viewBox="0 0 340 196" aria-hidden="true">
        <line x1="18" y1="78" x2="108" y2="78" stroke="#111214" stroke-width="2"/>
        <circle cx="120" cy="68" r="12" fill="none" stroke="#111214" stroke-width="2"/>
        <line x1="132" y1="78" x2="322" y2="78" stroke="#111214" stroke-width="2"/>
      </svg>
      <div style="position:absolute;left:22px;top:16px;display:flex;flex-direction:column;gap:5px;align-items:flex-start">
        <span class="mark-dot" style="width:14px;height:14px"></span>
        <span class="wordmark" style="font-size:10px">Lanterne<small>Architecture</small></span>
      </div>
      <div class="person" style="left:140px;top:44px;text-align:left">
        <div class="name" style="font-size:12px">Derek Tolson</div>
      </div>
      <div class="person" style="left:140px;top:84px;text-align:left">
        <div class="role">Director</div>
      </div>
      <ul class="contacts" style="left:140px;top:104px">
        <li><svg viewBox="0 0 10 10"><circle cx="5" cy="5" r="4.4" fill="none" stroke="#111214" stroke-width=".8"/><path d="M3.4 3h1l.4 1-.6.5a3 3 0 0 0 1.3 1.3l.5-.6 1 .4v1a.6.6 0 0 1-.6.6A3.6 3.6 0 0 1 2.8 3.6.6.6 0 0 1 3.4 3z" fill="#111214"/></svg>0279164073</li>
        <li><svg viewBox="0 0 10 10"><circle cx="5" cy="3.2" r="1.8" fill="none" stroke="#111214" stroke-width=".9"/><path d="M1.5 9a3.5 3 0 0 1 7 0" fill="none" stroke="#111214" stroke-width=".9"/></svg>@lanternearchitecture</li>
        <li><svg viewBox="0 0 10 10"><circle cx="5" cy="5" r="4.2" fill="none" stroke="#111214" stroke-width=".9"/><path d="M1 5h8M5 .8c-2 2.4-2 6 0 8.4M5 .8c2 2.4 2 6 0 8.4" fill="none" stroke="#111214" stroke-width=".7"/></svg>www.lanternearchitecture-example.co.nz</li>
        <li><svg viewBox="0 0 10 10"><circle cx="5" cy="5" r="4.2" fill="none" stroke="#111214" stroke-width=".9"/><circle cx="5" cy="5" r="2" fill="none" stroke="#111214" stroke-width=".9"/></svg>info@lanternearchitecture-example.co.nz</li>
      </ul>
    </div>
  </section>

  <section class="cell">
    <div class="card card-front-name">
      <svg class="rule" viewBox="0 0 340 196" aria-hidden="true">
        <line x1="22" y1="72" x2="122" y2="72" stroke="#111214" stroke-width="2"/>
        <circle cx="134" cy="62" r="12" fill="none" stroke="#111214" stroke-width="2"/>
        <line x1="146" y1="72" x2="318" y2="72" stroke="#111214" stroke-width="2"/>
      </svg>
      <div class="person" style="left:24px;top:26px;text-align:left">
        <div class="name">Derek Tolson</div>
        <div class="role" style="padding-left:24px">Director</div>
      </div>
      <ul class="contacts" style="left:150px;top:86px">
        <li><svg viewBox="0 0 10 10"><circle cx="5" cy="5" r="4.4" fill="none" stroke="#111214" stroke-width=".8"/><path d="M3.4 3h1l.4 1-.6.5a3 3 0 0 0 1.3 1.3l.5-.6 1 .4v1a.6.6 0 0 1-.6.6A3.6 3.6 0 0 1 2.8 3.6.6.6 0 0 1 3.4 3z" fill="#111214"/></svg>0279164073</li>
        <li><svg viewBox="0 0 10 10"><circle cx="5" cy="3.2" r="1.8" fill="none" stroke="#111214" stroke-width=".9"/><path d="M1.5 9a3.5 3 0 0 1 7 0" fill="none" stroke="#111214" stroke-width=".9"/></svg>@lanternearchitecture</li>
        <li><svg viewBox="0 0 10 10"><circle cx="5" cy="5" r="4.2" fill="none" stroke="#111214" stroke-width=".9"/><path d="M1 5h8M5 .8c-2 2.4-2 6 0 8.4M5 .8c2 2.4 2 6 0 8.4" fill="none" stroke="#111214" stroke-width=".7"/></svg>www.lanternearchitecture-example.co.nz</li>
        <li><svg viewBox="0 0 10 10"><circle cx="5" cy="5" r="4.2" fill="none" stroke="#111214" stroke-width=".9"/><circle cx="5" cy="5" r="2" fill="none" stroke="#111214" stroke-width=".9"/></svg>info@lanternearchitecture-example.co.nz</li>
      </ul>
    </div>
  </section>

</main>
</body>
</html>
```